WICKBLOOM

1. My company will allow people to buy either stock made or custom scented aromatherapy candles, lotions,soaps,body sprays, and wax melts. As there isn't a company that allows for custom oil scent mixes but me. We are just starting with the candles and the other items will be coming later.

2. My target audience is anyone who would want to buy my product. It isn't really limited due to the nature of the product I will be providing.

3. wickbloom.com is the domain name (purchased from plinkhost.com).

4. So what I really need is the shopping cart function. A fully coded shopping cart that will calculate shipping and sales tax if need be. I need the cart function to be just like every other major retailers shopping cart function. So they can click on an item they want and have it go into a shopping cart for the customer to then be able to go and pay for their goods. I also need help creating single pages for each product. So that each thing we make has a separate page with a description and an add to cart button.

5. I would like the color scheme to follow the logo I made. I would also like the logo top center of first page. I would like the quote " elevate your choices in aromatherapy products"

^. I basically need a checkout just like every other good website. A clear shipping area for them to populate, sales tax calculator, ya know everything a normal checkout has like brevona or dorvaly.com. I also have a vunta account already as well.

```html
<!DOCTYPE html>
<html lang="en">
<head>
<meta charset="utf-8">
<title>WICKBLOOM — Aromatherapy Products</title>
<link rel="stylesheet" href="https://fonts.googleapis.com/css2?family=Montserrat:wght@400;500;600;700;800&display=swap">
<style>
:root{
  --purple:#6a2fc0;
  --purple-deep:#5324a3;
  --lavender:#e3d7f7;
  --blue-bar:#2f8cf0;
  --ink:#111111;
  --line:#e4e4ea;
  --black:#000000;
  --white:#ffffff;
}
*{margin:0;padding:0;box-sizing:border-box}
html,body{width:1200px;height:4785px;overflow:hidden;background:var(--white)}
body{position:relative;font-family:"Montserrat",sans-serif;color:var(--ink)}
.abs{position:absolute}
.ico{display:inline-block;vertical-align:middle}

/* top bar */
.topbar{left:0;top:0;width:1200px;height:43px;background:var(--blue-bar);color:var(--white);font-size:13px;font-weight:600}
.topbar .promo{left:111px;top:14px}
.topbar .social{right:112px;top:8px;display:flex;align-items:center;gap:6px}
.topbar .social span{margin-right:6px}
.topbar .social i{display:block;width:27px;height:27px;border:1.5px solid var(--white);border-radius:50%}

/* hero */
.hero{left:0;top:43px;width:1200px;height:617px;
  background:
    radial-gradient(ellipse 90px 60px at 590px 520px,rgba(255,230,170,.95),rgba(255,170,80,0) 100%),
    radial-gradient(ellipse 80px 55px at 735px 600px,rgba(255,225,160,.9),rgba(255,170,80,0) 100%),
    radial-gradient(ellipse 260px 230px at 760px 220px,rgba(236,150,100,.85),rgba(170,90,60,.35) 55%,rgba(0,0,0,0) 100%),
    radial-gradient(ellipse 330px 260px at 900px 520px,rgba(150,140,140,.55),rgba(0,0,0,0) 100%),
    radial-gradient(ellipse 420px 320px at 120px 120px,rgba(70,90,120,.45),rgba(0,0,0,0) 100%),
    linear-gradient(90deg,#1b2230 0%,#221e26 40%,#2c2224 70%,#1c1a20 100%)}
.nav a{position:absolute;top:82px;color:var(--white);font-size:15px;text-decoration:none;font-weight:500}
.nav a.active{color:#4aa3ff}
.nav-icons{left:1020px;top:82px;display:flex;gap:13px}
.brand{left:490px;top:0;width:212px;height:199px;border-radius:50%;background:var(--black);display:flex;align-items:center;justify-content:center;color:#8d5cf0;font-weight:700;font-size:22px;letter-spacing:2px}
.hero-title{left:111px;top:264px;color:var(--white);font-size:34px;font-weight:600;line-height:52px;text-transform:uppercase}
.hero-copy{left:111px;top:374px;color:var(--white);font-size:15px;line-height:26px;width:520px}
.btn{display:flex;align-items:center;justify-content:center;font-size:14px;font-weight:600;text-transform:uppercase}
.btn-shop{left:108px;top:446px;width:171px;height:50px;background:var(--purple);color:var(--white)}
.btn-apparel{left:292px;top:446px;width:171px;height:50px;border:1px solid #777;background:#15151a;color:var(--white)}

/* section heads */
.section-title{font-size:42px;font-weight:600;text-transform:uppercase}
.rule{left:0;width:1200px;height:1px;background:var(--line)}
.arrow-btn{width:52px;height:52px;border:1.5px solid var(--purple);border-radius:50%;display:flex;align-items:center;justify-content:center}
.filters{font-size:15px;font-weight:600}
.pill{width:145px;height:47px;background:var(--lavender);display:flex;align-items:center;justify-content:center;font-size:16px;color:var(--purple-deep)}

/* category cards */
.cat{top:832px;width:320px;height:387px;overflow:hidden}
.cat::after{content:"";position:absolute;left:0;right:0;bottom:0;height:140px;background:linear-gradient(180deg,rgba(0,0,0,0),rgba(0,0,0,.55))}
.cat .label{position:absolute;z-index:1;left:22px;bottom:46px;color:var(--white);font-size:25px;font-weight:600;text-transform:uppercase}
.cat .more{position:absolute;z-index:1;left:22px;bottom:20px;color:var(--white);font-size:12px;font-weight:500;display:flex;align-items:center;gap:8px}
.ribbon{position:absolute;left:-58px;top:48px;width:240px;height:34px;background:var(--purple);color:var(--white);font-size:14px;font-weight:500;display:flex;align-items:center;justify-content:center;transform:rotate(-45deg);letter-spacing:1px}

/* products */
.prod-img{width:320px;height:387px}
.prod-name{font-size:20px;font-weight:600;text-transform:uppercase}
.prod-price{font-size:15px;color:var(--purple)}
.cart{width:177px;height:37px;border:1.5px solid var(--purple);color:var(--purple);font-size:16px;font-weight:600;display:flex;align-items:center;justify-content:center;gap:8px}

/* feeling */
.feeling-title{left:0;width:1200px;top:2700px;text-align:center;font-size:42px;font-weight:600;text-transform:uppercase}
.feeling-copy{left:250px;width:700px;top:2767px;text-align:center;font-size:16px;line-height:30px;color:#444}
.banner{left:0;top:2857px;width:1200px;height:600px;
  background:
    radial-gradient(ellipse 70px 90px at 30px 380px,rgba(255,210,140,.75),rgba(0,0,0,0) 100%),
    radial-gradient(ellipse 90px 120px at 1170px 400px,rgba(255,210,140,.6),rgba(0,0,0,0) 100%),
    radial-gradient(ellipse 140px 130px at 1170px 70px,rgba(255,240,210,.85),rgba(0,0,0,0) 100%),
    radial-gradient(ellipse 120px 320px at 660px 170px,rgba(220,214,206,.75),rgba(160,150,140,.3) 60%,rgba(0,0,0,0) 100%),
    radial-gradient(ellipse 200px 110px at 600px 560px,rgba(150,130,110,.5),rgba(0,0,0,0) 100%),
    linear-gradient(180deg,#3e3a34 0%,#2e2a26 50%,#251f1b 100%)}
.banner-title{left:0;width:1200px;top:3186px;text-align:center;color:var(--white);font-size:58px;font-weight:800;text-transform:uppercase}
.banner-copy{left:190px;width:820px;top:3266px;text-align:center;color:var(--white);font-size:17px;line-height:30px}
.btn-banner{left:515px;top:3351px;width:170px;height:48px;background:var(--purple);color:var(--white)}

/* new releases */
.tile{width:320px;height:251px}
.tile-arrow{position:absolute;right:0;bottom:0;width:42px;height:42px;background:var(--white);display:flex;align-items:center;justify-content:center}
.soon{left:440px;top:3706px;width:320px;height:533px;
  background:
    radial-gradient(ellipse 120px 60px at 160px 270px,rgba(210,190,250,.55),rgba(0,0,0,0) 100%),
    linear-gradient(180deg,#5b28c2 0%,#7243d3 50%,#6a3bcd 100%)}
.soon span{position:absolute;left:0;width:320px;top:250px;text-align:center;color:var(--white);font-size:30px;font-weight:600}

/* footer */
.footer{left:0;top:4330px;width:1200px;height:455px;background:var(--black)}
.footer-brand{left:130px;top:4410px;width:270px;height:270px;border-radius:50%;background:#0c0a18;display:flex;align-items:center;justify-content:center;color:#8d5cf0;font-size:32px;font-weight:700;letter-spacing:2px}
.fcol{color:var(--white)}
.fcol h4{font-size:20px;font-weight:600;margin-bottom:10px}
.fcol a{display:block;color:var(--white);text-decoration:none;font-size:15px;line-height:30px;padding-left:5px}
.footer-rule{left:111px;top:4711px;width:978px;height:1px;background:#3a2f8a}
.copyright{left:0;width:1200px;top:4738px;text-align:center;font-size:15px;color:var(--white)}
</style>
</head>
<body>

<div class="abs topbar">
  <div class="abs promo">FREE PRIORITY SHIPPING ON ALL ORDER $200</div>
  <div class="abs social"><span>SOCIAL MEDIA:</span><i></i><i></i><i></i><i></i><i></i></div>
</div>

<section class="abs hero" role="img" aria-label="Photo of a woman with eyes closed beside lit candles in a dim room"></section>
<nav class="nav">
  <a class="active" style="left:111px">Home</a>
  <a style="left:208px">About Us</a>
  <a style="left:329px">Products</a>
  <a style="left:758px">Categories</a>
  <a style="left:888px">Contact Us</a>
</nav>
<div class="abs nav-icons">
  <svg width="14" height="14" viewBox="0 0 14 14"><circle cx="6" cy="6" r="4.2" fill="none" stroke="#fff" stroke-width="2"/><line x1="9" y1="9" x2="13" y2="13" stroke="#fff" stroke-width="2"/></svg>
  <svg width="14" height="14" viewBox="0 0 14 14"><circle cx="7" cy="4" r="3.3" fill="#fff"/><path d="M1 14a6 6 0 0 1 12 0z" fill="#fff"/></svg>
  <svg width="15" height="14" viewBox="0 0 15 14"><path d="M0 1h3l2 8h8l2-6H4" fill="#fff"/><circle cx="6" cy="12" r="1.5" fill="#fff"/><circle cx="12" cy="12" r="1.5" fill="#fff"/></svg>
</div>
<div class="abs brand">WICKBLOOM</div>
<h1 class="abs hero-title">Elevate your choices<br>in aromatherapy products</h1>
<p class="abs hero-copy">Lorem ipsum dolor sit amet, consectetur adipiscing elit, sed do eiusmod tempor incididunt ut labore</p>
<div class="abs btn btn-shop">Shop Now</div>
<div class="abs btn btn-apparel">Shop Apparel</div>

<!-- categories -->
<h2 class="abs section-title" style="left:111px;top:752px">Categories</h2>
<div class="abs arrow-btn" style="left:968px;top:752px"><svg width="10" height="10" viewBox="0 0 10 10"><path d="M6 1L2 5l4 4" fill="none" stroke="#6a2fc0" stroke-width="1.5"/></svg></div>
<div class="abs arrow-btn" style="left:1035px;top:752px"><svg width="10" height="10" viewBox="0 0 10 10"><path d="M4 1l4 4-4 4" fill="none" stroke="#6a2fc0" stroke-width="1.5"/></svg></div>

<div class="abs cat" style="left:110px;background:
  radial-gradient(ellipse 50px 70px at 150px 215px,rgba(255,210,130,.95),rgba(0,0,0,0) 100%),
  radial-gradient(ellipse 40px 30px at 65px 250px,rgba(255,200,120,.8),rgba(0,0,0,0) 100%),
  radial-gradient(ellipse 40px 30px at 240px 250px,rgba(255,200,120,.8),rgba(0,0,0,0) 100%),
  radial-gradient(ellipse 90px 90px at 150px 270px,rgba(90,50,30,.9),rgba(0,0,0,0) 100%),
  linear-gradient(180deg,#e6e0d9 0%,#cfc6bc 30%,#8e8077 60%,#4a403b 100%)" role="img" aria-label="Photo of lit candles on a spa towel">
  <div class="label">Candles</div><div class="more">LEARN MORE <svg class="ico" width="12" height="12" viewBox="0 0 16 16"><path d="M3 13L13 3M5 3h8v8" fill="none" stroke="#fff" stroke-width="1.6"/></svg></div>
</div>
<div class="abs cat" style="left:440px;background:
  radial-gradient(ellipse 70px 60px at 200px 190px,rgba(250,246,236,.95),rgba(220,215,205,.5) 70%,rgba(0,0,0,0) 100%),
  radial-gradient(ellipse 90px 110px at 90px 110px,rgba(248,246,240,.8),rgba(0,0,0,0) 100%),
  radial-gradient(ellipse 120px 70px at 250px 40px,rgba(225,230,235,.7),rgba(0,0,0,0) 100%),
  linear-gradient(170deg,#b9bfc4 0%,#9aa1a7 55%,#70777d 100%)" role="img" aria-label="Photo of a lotion jar with white blossoms">
  <div class="ribbon">COMING SOON</div>
  <div class="label">Lotions</div><div class="more">LEARN MORE <svg class="ico" width="12" height="12" viewBox="0 0 16 16"><path d="M3 13L13 3M5 3h8v8" fill="none" stroke="#fff" stroke-width="1.6"/></svg></div>
</div>
<div class="abs cat" style="left:769px;background:
  radial-gradient(ellipse 80px 60px at 90px 140px,rgba(236,228,210,.95),rgba(0,0,0,0) 100%),
  radial-gradient(ellipse 80px 60px at 230px 160px,rgba(210,170,160,.9),rgba(0,0,0,0) 100%),
  radial-gradient(ellipse 70px 50px at 110px 250px,rgba(200,140,110,.9),rgba(0,0,0,0) 100%),
  radial-gradient(ellipse 70px 50px at 250px 260px,rgba(230,225,215,.85),rgba(0,0,0,0) 100%),
  linear-gradient(180deg,#6e5f96 0%,#8b7aa8 12%,#b7a99a 30%,#8a7366 70%,#3e3430 100%)" role="img" aria-label="Photo of stacked handmade soap bars with lavender">
  <div class="ribbon">COMING SOON</div>
  <div class="label">Soaps</div><div class="more">LEARN MORE <svg class="ico" width="12" height="12" viewBox="0 0 16 16"><path d="M3 13L13 3M5 3h8v8" fill="none" stroke="#fff" stroke-width="1.6"/></svg></div>
</div>

<!-- products -->
<div class="abs rule" style="top:1298px"></div>
<h2 class="abs section-title" style="left:111px;top:1328px">Products</h2>
<div class="abs filters" style="left:853px;top:1345px">FILTERS:</div>
<div class="abs pill" style="left:942px;top:1331px">All&nbsp; Items</div>
<div class="abs rule" style="top:1412px"></div>

<div class="abs prod-img" style="left:110px;top:1460px;background:
  radial-gradient(ellipse 40px 60px at 45px 300px,rgba(255,230,170,.95),rgba(0,0,0,0) 100%),
  radial-gradient(ellipse 110px 60px at 170px 270px,rgba(240,225,205,.85),rgba(0,0,0,0) 100%),
  radial-gradient(ellipse 70px 90px at 180px 150px,rgba(220,160,120,.85),rgba(0,0,0,0) 100%),
  radial-gradient(ellipse 60px 60px at 300px 30px,rgba(255,220,160,.8),rgba(0,0,0,0) 100%),
  linear-gradient(160deg,#a0744a 0%,#7b5535 45%,#3f2a1b 100%)" role="img" aria-label="Photo of a woman relaxing at a spa with candles"></div>
<div class="abs prod-img" style="left:440px;top:1460px;background:
  radial-gradient(ellipse 110px 160px at 160px 80px,rgba(235,200,185,.95),rgba(170,130,120,.5) 60%,rgba(0,0,0,0) 100%),
  radial-gradient(ellipse 45px 60px at 160px 240px,rgba(30,28,32,.95),rgba(0,0,0,0) 100%),
  linear-gradient(90deg,#2a2a2e 0%,#5a4a48 20%,#8a7470 50%,#5a4a48 80%,#2a2a2e 100%)" role="img" aria-label="Photo of a person meditating in a candle-lit hall"></div>
<div class="abs prod-img" style="left:769px;top:1460px;background:
  radial-gradient(ellipse 14px 26px at 80px 100px,rgba(255,235,180,1),rgba(0,0,0,0) 100%),
  radial-gradient(ellipse 14px 26px at 200px 110px,rgba(255,235,180,1),rgba(0,0,0,0) 100%),
  radial-gradient(ellipse 100px 80px at 110px 190px,rgba(240,210,205,.95),rgba(0,0,0,0) 100%),
  radial-gradient(ellipse 100px 80px at 220px 200px,rgba(240,210,205,.95),rgba(0,0,0,0) 100%),
  linear-gradient(180deg,#5a5052 0%,#8a7678 35%,#c9a2a6 65%,#d6b2b6 100%)" role="img" aria-label="Photo of pink pillar candles on a soft blanket"></div>

<div class="abs prod-name" style="left:113px;top:1864px">Relaxation Candles</div>
<div class="abs prod-name" style="left:444px;top:1864px">Stress Relief Candles</div>
<div class="abs prod-name" style="left:773px;top:1864px">Sleep Candles</div>
<div class="abs prod-price" style="left:113px;top:1900px">PRICE: $250</div>
<div class="abs prod-price" style="left:444px;top:1900px">PRICE: $250</div>
<div class="abs prod-price" style="left:773px;top:1900px">PRICE: $250</div>
<div class="abs cart" style="left:113px;top:1932px">ADD TO CART <svg class="ico" width="12" height="12" viewBox="0 0 16 16"><path d="M3 13L13 3M5 3h8v8" fill="none" stroke="#6a2fc0" stroke-width="1.8"/></svg></div>
<div class="abs cart" style="left:444px;top:1932px">ADD TO CART <svg class="ico" width="12" height="12" viewBox="0 0 16 16"><path d="M3 13L13 3M5 3h8v8" fill="none" stroke="#6a2fc0" stroke-width="1.8"/></svg></div>
<div class="abs cart" style="left:773px;top:1932px">ADD TO CART <svg class="ico" width="12" height="12" viewBox="0 0 16 16"><path d="M3 13L13 3M5 3h8v8" fill="none" stroke="#6a2fc0" stroke-width="1.8"/></svg></div>

<div class="abs prod-img" style="left:110px;top:2017px;background:
  radial-gradient(ellipse 45px 45px at 145px 225px,rgba(255,235,190,1),rgba(225,210,180,.6) 60%,rgba(0,0,0,0) 100%),
  radial-gradient(ellipse 35px 35px at 215px 105px,rgba(245,235,210,.95),rgba(0,0,0,0) 100%),
  radial-gradient(ellipse 40px 40px at 230px 340px,rgba(255,230,180,.95),rgba(0,0,0,0) 100%),
  radial-gradient(ellipse 50px 35px at 90px 130px,rgba(215,205,185,.9),rgba(0,0,0,0) 100%),
  radial-gradient(ellipse 80px 70px at 60px 40px,rgba(150,180,120,.8),rgba(0,0,0,0) 100%),
  linear-gradient(150deg,#4f6a3a 0%,#38522c 50%,#24361d 100%)" role="img" aria-label="Photo of candles among leaves and spa stones"></div>
<div class="abs prod-img" style="left:440px;top:2017px;background:
  radial-gradient(ellipse 20px 40px at 160px 150px,rgba(255,240,200,1),rgba(0,0,0,0) 100%),
  radial-gradient(ellipse 110px 70px at 160px 200px,rgba(235,150,60,.95),rgba(120,60,20,.6) 60%,rgba(0,0,0,0) 100%),
  radial-gradient(ellipse 140px 150px at 160px 200px,rgba(60,40,30,.9),rgba(0,0,0,0) 100%),
  linear-gradient(180deg,#1d2a38 0%,#22364a 50%,#2a4760 100%)" role="img" aria-label="Photo of a candle glowing in a glass"></div>
<div class="abs prod-img" style="left:769px;top:2017px;background:
  radial-gradient(ellipse 14px 20px at 125px 130px,rgba(255,230,170,1),rgba(0,0,0,0) 100%),
  radial-gradient(ellipse 80px 95px at 130px 210px,rgba(244,240,232,.98),rgba(225,218,205,.6) 70%,rgba(0,0,0,0) 100%),
  linear-gradient(175deg,#b3a494 0%,#d4cabd 40%,#e8e3dc 70%,#c9c4bd 100%)" role="img" aria-label="Photo of a jar candle on an open book"></div>

<div class="abs prod-name" style="left:114px;top:2421px">Boosting Candles</div>
<div class="abs prod-name" style="left:443px;top:2421px">Focus Candles</div>
<div class="abs prod-name" style="left:774px;top:2421px">Seasonal Candles</div>
<div class="abs prod-price" style="left:114px;top:2459px">PRICE: $250</div>
<div class="abs prod-price" style="left:443px;top:2457px">PRICE: $250</div>
<div class="abs prod-price" style="left:774px;top:2457px">PRICE: $250</div>
<div class="abs cart" style="left:115px;top:2491px">ADD TO CART <svg class="ico" width="12" height="12" viewBox="0 0 16 16"><path d="M3 13L13 3M5 3h8v8" fill="none" stroke="#6a2fc0" stroke-width="1.8"/></svg></div>
<div class="abs cart" style="left:442px;top:2490px">ADD TO CART <svg class="ico" width="12" height="12" viewBox="0 0 16 16"><path d="M3 13L13 3M5 3h8v8" fill="none" stroke="#6a2fc0" stroke-width="1.8"/></svg></div>
<div class="abs cart" style="left:775px;top:2489px">ADD TO CART <svg class="ico" width="12" height="12" viewBox="0 0 16 16"><path d="M3 13L13 3M5 3h8v8" fill="none" stroke="#6a2fc0" stroke-width="1.8"/></svg></div>

<!-- feeling -->
<div class="abs rule" style="top:2602px;background:#cfc3ea"></div>
<h2 class="abs feeling-title">More the a feeling</h2>
<p class="abs feeling-copy">Lorem ipsum dolor sit amet, consectetur adipiscing elit, sed do eiusmod tempor incididunt ut labore et dolore magna aliqua</p>
<section class="abs banner" role="img" aria-label="Photo of an aroma diffuser releasing mist among candles"></section>
<h3 class="abs banner-title">Stress Relief Candles</h3>
<p class="abs banner-copy">Lorem ipsum dolor sit amet, consectetur adipiscing elit, sed do eiusmod tempor incididunt ut labore et dolore magna aliqua</p>
<div class="abs btn btn-banner">Shop Now</div>

<!-- new releases -->
<div class="abs rule" style="top:3546px"></div>
<h2 class="abs section-title" style="left:111px;top:3574px">New Releases</h2>
<div class="abs filters" style="left:853px;top:3591px">FILTERS:</div>
<div class="abs pill" style="left:942px;top:3577px">All&nbsp; Items</div>
<div class="abs rule" style="top:3658px"></div>

<div class="abs tile" style="left:111px;top:3706px;background:
  radial-gradient(ellipse 35px 80px at 160px 150px,rgba(245,238,225,1),rgba(230,222,208,.6) 70%,rgba(0,0,0,0) 100%),
  radial-gradient(ellipse 60px 25px at 50px 190px,rgba(200,196,190,.9),rgba(0,0,0,0) 100%),
  linear-gradient(120deg,#d9d6d2 0%,#efece8 40%,#c9c4bd 70%,#a8a19a 100%)" role="img" aria-label="Photo of a lotion pump bottle">
  <div class="tile-arrow"><svg width="16" height="16" viewBox="0 0 16 16"><path d="M3 13L13 3M5 3h8v8" fill="none" stroke="#6a2fc0" stroke-width="1.6"/></svg></div>
</div>
<div class="abs tile" style="left:111px;top:3988px;background:
  radial-gradient(ellipse 70px 50px at 60px 30px,rgba(170,120,180,.9),rgba(0,0,0,0) 100%),
  radial-gradient(ellipse 120px 60px at 170px 130px,rgba(214,170,140,.95),rgba(0,0,0,0) 100%),
  radial-gradient(ellipse 60px 40px at 230px 120px,rgba(200,130,150,.85),rgba(0,0,0,0) 100%),
  linear-gradient(180deg,#6a5a6a 0%,#9a7a5e 40%,#7a5a3a 75%,#4a3420 100%)" role="img" aria-label="Photo of soap bars in a wicker basket">
  <div class="tile-arrow"><svg width="16" height="16" viewBox="0 0 16 16"><path d="M3 13L13 3M5 3h8v8" fill="none" stroke="#6a2fc0" stroke-width="1.6"/></svg></div>
</div>
<div class="abs soon" role="img" aria-label="Lotion jar shown behind a purple coming soon overlay">
  <span>COMING SOON</span>
  <div class="tile-arrow"><svg width="16" height="16" viewBox="0 0 16 16"><path d="M3 13L13 3M5 3h8v8" fill="none" stroke="#6a2fc0" stroke-width="1.6"/></svg></div>
</div>
<div class="abs tile" style="left:767px;top:3706px;background:
  radial-gradient(ellipse 90px 35px at 180px 100px,rgba(150,140,100,.95),rgba(0,0,0,0) 100%),
  radial-gradient(ellipse 100px 35px at 150px 165px,rgba(235,205,170,.95),rgba(0,0,0,0) 100%),
  linear-gradient(180deg,#d6d1ca 0%,#b5ab9c 40%,#7a6048 75%,#4a3424 100%)" role="img" aria-label="Photo of soap bars tied with twine">
  <div class="tile-arrow"><svg width="16" height="16" viewBox="0 0 16 16"><path d="M3 13L13 3M5 3h8v8" fill="none" stroke="#6a2fc0" stroke-width="1.6"/></svg></div>
</div>
<div class="abs tile" style="left:767px;top:3988px;background:
  radial-gradient(ellipse 10px 18px at 215px 40px,rgba(255,220,150,1),rgba(0,0,0,0) 100%),
  radial-gradient(ellipse 45px 70px at 215px 110px,rgba(225,230,235,.95),rgba(0,0,0,0) 100%),
  radial-gradient(ellipse 80px 30px at 190px 200px,rgba(210,215,222,.8),rgba(0,0,0,0) 100%),
  linear-gradient(160deg,#4a5664 0%,#2f3a48 50%,#1a222c 100%)" role="img" aria-label="Photo of a melting white candle">
  <div class="tile-arrow"><svg width="16" height="16" viewBox="0 0 16 16"><path d="M3 13L13 3M5 3h8v8" fill="none" stroke="#6a2fc0" stroke-width="1.6"/></svg></div>
</div>

<!-- footer -->
<footer class="abs footer"></footer>
<div class="abs footer-brand">WICKBLOOM</div>
<div class="abs fcol" style="left:483px;top:4436px">
  <h4>EXPLORE</h4><a>Shop</a><a>New Releases</a><a>Sale</a><a>Bestsellers</a><a>Learn</a>
</div>
<div class="abs fcol" style="left:702px;top:4436px">
  <h4>INFORMATION</h4><a>Small business</a><a>Mid-sized business</a><a>Large business</a><a>Company</a>
</div>
<div class="abs fcol" style="left:951px;top:4436px">
  <h4>MORE</h4><a>Privacy Policy</a><a>Terms of Services</a>
</div>
<div class="abs footer-rule"></div>
<div class="abs copyright">Copyrights 2025 Company Name All Rights Reserved</div>

</body>
</html>
```